Bref créative
Newspaper Ad for Immigration Law Firm
Need Three Ads/Sizes
I need a total of 3 newspaper ads with 3 different sizes.
1. Main Ad - 5 in x 2 in
2. 3.25 in x 2 in
3. 1.5 in x 2 in
Designers should submit their design based on the 5 in x 2 in. Once I have determined the "winning designer," I will work with that designer to create the other two ads using the same winning design.
Law
The following must be included: I will also upload my picture, my logo, and Board Certified Logo. Thanks.
1. Picture of Attorney
2. Attorney
3. Brian K. Wendell
4. Law Firm logo
5. Board Certified Logo
6. Immigration Law below Board Certified Logo
7. 4180 Millbrook Lane
8. Suite 318
9. Houston, Texas 77043
10. www.thewendellcounsel.com
11. Telephone: (713) 548-2190
12. Fax: (713) 548-2197
13. bkellan4471@mailvexo.com
14. Immigration Bonds
15. Deportation Cases
16. Immigration Court
17. Immigration Waivers
18. Immigration Appeals
19. Family Petitions
20. Citizenship
21. Permanent Residency
22. Asylum, TPS, NACARA
23. Work Permits
24. Other Immigration Cases
Law Firm Logo Should go on the very top i think
You can cut out background if you like. Or not, up to your design.
The phrase "Immigration Law" must be directly underneath this logo. Logo cannot be changed or altered.
Sample proof

```html
<!DOCTYPE html>
<html lang="en">
<head>
<meta charset="utf-8">
<title>Newspaper Ad – Law Office of Brian K. Wendell</title>
<link rel="stylesheet" href="https://fonts.googleapis.com/css2?family=Cinzel:wght@600&family=Oswald:wght@400&family=PT+Serif:wght@400;700&display=swap">
<style>
  :root{
    --board-top:#5a5a5a;
    --board-bottom:#141414;
    --board-text:#b9b9b9;
    --paper:#ffffff;
    --navy:#1d2a5a;
    --accent:#9a1f1a;
    --band-light:#6a231c;
    --band-dark:#2a0b08;
    --photo-light:#7b8494;
    --photo-dark:#2c2f38;
    --ink:#111111;
    --service-text:#ffffff;
  }
  *{box-sizing:border-box;margin:0;padding:0}
  html,body{width:1200px;height:901px;overflow:hidden}
  body{
    background:radial-gradient(ellipse at 50% 35%,var(--board-top) 0%,#2e2e2e 55%,var(--board-bottom) 100%);
    font-family:"PT Serif",serif;
    position:relative;
  }
  .board-label{position:absolute;left:15px;top:22px;color:var(--board-text);font:400 16px "Oswald",sans-serif;letter-spacing:.3px}
  .board-note{position:absolute;left:910px;top:512px;color:#9a9a9a;font:400 14px/20px "PT Serif",serif}
  .board-caption{position:absolute;left:718px;top:852px;color:#8a8a8a;font:400 14px "PT Serif",serif}

  .ad{
    position:absolute;width:584px;height:365px;background:var(--paper);
    border:1px solid #333;overflow:hidden;transform-origin:0 0;
    box-shadow:0 6px 18px rgba(0,0,0,.45);
  }
  .ad--color{left:309px;top:219px}
  .ad--mono{
    left:718px;top:596px;transform:scale(.666);
    --navy:#222;--accent:#222;--band-light:#3c3c3c;--band-dark:#151515;
    --photo-light:#8a8a8a;--photo-dark:#2e2e2e;
  }

  .ad__brand{position:absolute;left:12px;top:8px;display:flex;align-items:center;gap:10px}
  .ad__brand-mark{width:46px;height:46px;border-radius:50%;background:var(--navy)}
  .ad__brand-text{color:var(--navy);font-family:"Cinzel",serif;font-weight:600;text-align:center;line-height:1.1}
  .ad__brand-pre{font-size:13px;letter-spacing:1px}
  .ad__brand-name{font-size:23px;letter-spacing:.5px}
  .ad__brand-sub{font-size:13px;letter-spacing:1px}

  .ad__cert{position:absolute;left:400px;top:8px;width:150px}
  .ad__cert-badge{display:flex;gap:4px;align-items:center}
  .ad__cert-square{width:24px;height:24px;background:var(--navy)}
  .ad__cert-bar{flex:1;height:16px;background:var(--navy);border-radius:2px}
  .ad__cert-area{margin-top:3px;color:var(--accent);font:700 11px "PT Serif",serif}

  .ad__services{
    position:absolute;left:0;top:68px;width:584px;height:237px;
    background:radial-gradient(ellipse at 30% 40%,var(--band-light) 0%,var(--band-dark) 100%);
  }
  .ad__list{position:absolute;top:14px;list-style:none;color:var(--service-text);font:400 17px/25px "Oswald",sans-serif;letter-spacing:.2px}
  .ad__list li::before{content:"•";margin-right:7px}
  .ad__list--left{left:12px}
  .ad__list--right{left:244px;width:172px}
  .ad__list .wrap{padding-left:13px;display:block;margin-top:-4px}

  .ad__photo{
    position:absolute;left:420px;top:66px;width:164px;height:239px;
    background:linear-gradient(180deg,var(--photo-light),var(--photo-dark));
  }
  .ad__photo-caption{position:absolute;left:420px;width:164px;top:278px;color:#fff;font:400 8.5px/10px "PT Serif",serif;text-align:center;letter-spacing:.5px}

  .ad__footer{position:absolute;left:0;top:305px;width:584px;height:60px;background:var(--paper)}
  .ad__phone{position:absolute;left:10px;top:9px;color:var(--ink);font:400 31px "PT Serif",serif;letter-spacing:.3px}
  .ad__address{position:absolute;left:290px;top:11px;color:var(--ink);font:400 9.5px/12.5px "PT Serif",serif;white-space:nowrap}
  .ad__web{letter-spacing:2px;font-size:11.5px}
</style>
</head>
<body>
  <div class="board-label">3.25" x 2" Newspaper Ad</div>

  <article class="ad ad--color">
    <div class="ad__brand">
      <span class="ad__brand-mark"></span>
      <div class="ad__brand-text">
        <div class="ad__brand-pre">Law Office of</div>
        <div class="ad__brand-name">BRIAN K. WENDELL</div>
        <div class="ad__brand-sub">IMMIGRATION LAW FIRM</div>
      </div>
    </div>
    <div class="ad__cert">
      <div class="ad__cert-badge"><span class="ad__cert-square"></span><span class="ad__cert-bar"></span></div>
      <div class="ad__cert-area">Immigration Law</div>
    </div>
    <section class="ad__services">
      <ul class="ad__list ad__list--left">
        <li>Immigration Bonds</li><li>Deportation Cases</li><li>Immigration Court</li>
        <li>Immigration Waivers</li><li>Immigration Appeals</li><li>Family Petitions</li>
      </ul>
      <ul class="ad__list ad__list--right">
        <li>Citizenship</li><li>Permanent Residency</li><li>Asylum, TPS, NACARA</li>
        <li>Work Permits</li><li>Other Immigration<span class="wrap">Cases</span></li>
      </ul>
    </section>
    <div class="ad__photo" role="img" aria-label="Portrait photo of attorney Brian K. Wendell"></div>
    <div class="ad__photo-caption">BRIAN K. WENDELL<br>ATTORNEY</div>
    <footer class="ad__footer">
      <div class="ad__phone">(713) 548-2190</div>
      <div class="ad__address">
        4180 Millbrook Lane Suite 318 Houston, Texas 77043<br>
        Fax: (713) 548-2197 &nbsp; Email: bkellan4471@mailvexo.com<br>
        <span class="ad__web">www.thewendellcounsel.com</span>
      </div>
    </footer>
  </article>

  <div class="board-note">solid white space<br>background to edge<br>image moved up a little</div>

  <article class="ad ad--mono">
    <div class="ad__brand">
      <span class="ad__brand-mark"></span>
      <div class="ad__brand-text">
        <div class="ad__brand-pre">Law Office of</div>
        <div class="ad__brand-name">BRIAN K. WENDELL</div>
        <div class="ad__brand-sub">IMMIGRATION LAW FIRM</div>
      </div>
    </div>
    <div class="ad__cert">
      <div class="ad__cert-badge"><span class="ad__cert-square"></span><span class="ad__cert-bar"></span></div>
      <div class="ad__cert-area">Immigration Law</div>
    </div>
    <section class="ad__services">
      <ul class="ad__list ad__list--left">
        <li>Immigration Bonds</li><li>Deportation Cases</li><li>Immigration Court</li>
        <li>Immigration Waivers</li><li>Immigration Appeals</li><li>Family Petitions</li>
      </ul>
      <ul class="ad__list ad__list--right">
        <li>Citizenship</li><li>Permanent Residency</li><li>Asylum, TPS, NACARA</li>
        <li>Work Permits</li><li>Other Immigration<span class="wrap">Cases</span></li>
      </ul>
    </section>
    <div class="ad__photo" role="img" aria-label="Black and white portrait photo of attorney Brian K. Wendell"></div>
    <div class="ad__photo-caption">BRIAN K. WENDELL<br>ATTORNEY</div>
    <footer class="ad__footer">
      <div class="ad__phone">(713) 548-2190</div>
      <div class="ad__address">
        4180 Millbrook Lane Suite 318 Houston, Texas 77043<br>
        Fax: (713) 548-2197 &nbsp; Email: bkellan4471@mailvexo.com<br>
        <span class="ad__web">www.thewendellcounsel.com</span>
      </div>
    </footer>
  </article>

  <div class="board-caption">Black &amp; White simulation</div>
</body>
</html>
```